design a original concept for a wine box set.

this will be a gift box for 2 of these wine bottles and 2 pens.as u will see the the design of the vessels for these wines are very cools and unique. it will be a set of 2 wines and 2 pens,wine MSRP for each bottle about 30.00 each.so with the2 wine and 2 pens in gift box we may upsell it got 100.00 or 120.00 retail.looking for a upscale box design,something different,edgy,catchy,glammy to pick up on the fun side of this wine

Industry/Entity Type

wines

Font styles to use
Serif
Decorative

Requirements
Must have
• high end box for my really cool vessels of my wines for cooperate sales for holidays and etc
Nice to have
• pick up the details for the unique design of my glass bottles of my wines and the diamond on the pen
Should not have
• a cheap feel

```html
<!DOCTYPE html>
<html lang="en">
<head>
<meta charset="utf-8">
<title>Vellantri Brut No7 – Gift Box Lid</title>
<link rel="stylesheet" href="https://fonts.googleapis.com/css2?family=Great+Vibes&family=Josefin+Sans:wght@400;600&family=Cinzel:wght@400;600&display=swap">
<style>
  :root {
    --backdrop: #23252a;
    --wood-dark: #3f3023;
    --wood-mid: #5b4632;
    --wood-light: #6e5640;
    --gold: #c9a15d;
    --gold-soft: rgba(201, 161, 93, 0.35);
  }
  html, body {
    margin: 0;
    padding: 0;
    width: 1200px;
    height: 849px;
    overflow: hidden;
    background: var(--backdrop);
  }
  .lid-canvas {
    width: 1200px;
    height: 849px;
    display: block;
  }
  .lid-frame-line {
    fill: none;
    stroke: var(--gold);
  }
  .lid-tagline {
    font-family: "Cinzel", serif;
    font-size: 20px;
    letter-spacing: 7px;
    fill: var(--gold);
  }
  .lid-number {
    font-family: "Josefin Sans", sans-serif;
    font-size: 34px;
    letter-spacing: 3px;
    fill: var(--gold);
  }
  .lid-brand {
    font-family: "Great Vibes", cursive;
    font-size: 128px;
    fill: var(--gold);
  }
  .lid-variety {
    font-family: "Josefin Sans", sans-serif;
    font-weight: 600;
    font-size: 44px;
    letter-spacing: 6px;
    fill: var(--gold);
  }
  .lid-corner-ornament {
    fill: var(--gold-soft);
  }
</style>
</head>
<body>
<svg class="lid-canvas" viewBox="0 0 1200 849" xmlns="http://www.w3.org/2000/svg">
  <defs>
    <linearGradient id="wood-surface" x1="0" y1="0" x2="1" y2="1">
      <stop offset="0" stop-color="#6e5640"/>
      <stop offset="0.5" stop-color="#5b4632"/>
      <stop offset="1" stop-color="#3f3023"/>
    </linearGradient>
    <path id="tagline-arc" d="M 385 330 Q 600 225 815 330"/>
    <path id="slogan-arc" d="M 385 550 Q 600 660 815 550"/>
  </defs>

  <!-- Lid panel -->
  <rect class="lid-panel" x="140" y="100" width="920" height="650" rx="4"
        fill="url(#wood-surface)" role="img" aria-label="Weathered wooden lid surface with visible grain"/>

  <!-- Frame: outer and inner rule with notched corners -->
  <path class="lid-frame-line" stroke-width="4"
        d="M 270 190 H 930 Q 930 230 970 230 V 620 Q 930 620 930 660 H 270 Q 270 620 230 620 V 230 Q 270 230 270 190 Z"/>
  <path class="lid-frame-line" stroke-width="1.5"
        d="M 280 202 H 920 Q 922 238 958 240 V 610 Q 922 612 920 648 H 280 Q 278 612 242 610 V 240 Q 278 238 280 202 Z"/>

  <!-- Corner filigree areas -->
  <rect class="lid-corner-ornament" x="250" y="215" width="125" height="105" rx="30" role="img" aria-label="Gold scrollwork filigree, top left corner"/>
  <rect class="lid-corner-ornament" x="825" y="215" width="125" height="105" rx="30" role="img" aria-label="Gold scrollwork filigree, top right corner"/>
  <rect class="lid-corner-ornament" x="250" y="530" width="125" height="105" rx="30" role="img" aria-label="Gold scrollwork filigree, bottom left corner"/>
  <rect class="lid-corner-ornament" x="825" y="530" width="125" height="105" rx="30" role="img" aria-label="Gold scrollwork filigree, bottom right corner"/>

  <!-- Text -->
  <text class="lid-tagline"><textPath href="#tagline-arc" startOffset="50%" text-anchor="middle">CLASSIC RICH TASTE</textPath></text>
  <text class="lid-number" x="600" y="350" text-anchor="middle">No7</text>
  <text class="lid-brand" x="600" y="460" text-anchor="middle">Vellantri</text>
  <text class="lid-variety" x="600" y="520" text-anchor="middle">BRUT</text>
  <text class="lid-tagline"><textPath href="#slogan-arc" startOffset="50%" text-anchor="middle">THE BEST CHOICE EVER</textPath></text>
</svg>
</body>
</html>
```